Wedding invitation

We need a wedding invitation designed with a logo using our initials and name underneath.
We are getting married at THE VERDELLE hotel in Gstaad and we would like have our logo similar to theirs but incorporating our initials n&l (any font/case) and our names below nuriya and Laurent. The Verdelle logo can be seen on their website.
The invitation would be square with the logo on the front in stamped foil and the colour would be THE VERDELLE brown (I have the exact colour)
THE VERDELLE Brown: C45 M70 Y68 K77
THE VERDELLE Rose Gold: BRENVIK 812
Inside we would have the invitation wording and on the opposite side some contact info. There would be four inserts - accom, directions, brunch and RSVP. We will provide the wording.

```html
<!DOCTYPE html>
<html lang="en">
<head>
<meta charset="utf-8">
<title>Directions — Wedding Insert</title>
<link rel="stylesheet" href="https://fonts.googleapis.com/css2?family=Gelasio:wght@400;700&family=Pinyon+Script&display=swap">
<style>
  :root {
    --paper: #ffffff;
    --rose: #b86c7b;
    --rose-text: #b46878;
    --rose-soft: #f3dfe3;
    --ink: #2a1512;
  }
  html, body {
    margin: 0;
    padding: 0;
    width: 1200px;
    height: 1200px;
    overflow: hidden;
    background: var(--paper);
  }
  .insert {
    position: relative;
    width: 1200px;
    height: 1200px;
    background: var(--paper);
    font-family: "Gelasio", Georgia, serif;
    color: var(--rose-text);
  }
  .insert__frame {
    position: absolute;
    inset: 0;
    width: 1200px;
    height: 1200px;
  }
  .insert__corner {
    position: absolute;
    width: 172px;
    height: 172px;
    background: radial-gradient(circle at center, var(--rose-soft) 0%, rgba(243,223,227,0.35) 60%, rgba(255,255,255,0) 100%);
  }
  .insert__corner--tl { left: 24px; top: 20px; }
  .insert__corner--tr { right: 24px; top: 20px; }
  .insert__corner--bl { left: 24px; bottom: 20px; }
  .insert__corner--br { right: 24px; bottom: 20px; }
  .insert__title {
    position: absolute;
    left: 0;
    right: 0;
    top: 92px;
    margin: 0;
    text-align: center;
    padding-right: 30px;
    font-family: "Pinyon Script", cursive;
    font-weight: 400;
    font-size: 112px;
    line-height: 1;
    color: var(--ink);
  }
  .insert__flourish {
    position: absolute;
    left: 444px;
    top: 228px;
    width: 300px;
    height: 56px;
    border-radius: 28px;
    background: linear-gradient(90deg, rgba(243,223,227,0) 0%, var(--rose-soft) 25%, var(--rose-soft) 75%, rgba(243,223,227,0) 100%);
  }
  .directions {
    position: absolute;
    left: 96px;
    width: 1040px;
  }
  .directions--airport { top: 380px; }
  .directions--driving { top: 710px; }
  .directions__heading {
    margin: 0;
    font-size: 27px;
    font-weight: 700;
    line-height: 1.3;
    color: var(--rose-text);
  }
  .directions__text {
    margin: 0;
    font-size: 27.5px;
    line-height: 38.6px;
    font-weight: 400;
    white-space: nowrap;
  }
  .directions--airport .directions__heading { margin-bottom: 12px; }
</style>
</head>
<body>
  <main class="insert">
    <svg class="insert__frame" viewBox="0 0 1200 1200" aria-hidden="true">
      <g stroke="var(--rose)" stroke-width="3" fill="none">
        <line x1="197" y1="25" x2="997" y2="25"/>
        <line x1="197" y1="33" x2="997" y2="33"/>
        <line x1="197" y1="1167" x2="997" y2="1167"/>
        <line x1="197" y1="1175" x2="997" y2="1175"/>
        <line x1="29" y1="195" x2="29" y2="1000"/>
        <line x1="37" y1="195" x2="37" y2="1000"/>
        <line x1="1163" y1="195" x2="1163" y2="1000"/>
        <line x1="1171" y1="195" x2="1171" y2="1000"/>
      </g>
    </svg>

    <div class="insert__corner insert__corner--tl" role="img" aria-label="Rose filigree corner ornament"></div>
    <div class="insert__corner insert__corner--tr" role="img" aria-label="Rose filigree corner ornament"></div>
    <div class="insert__corner insert__corner--bl" role="img" aria-label="Rose filigree corner ornament"></div>
    <div class="insert__corner insert__corner--br" role="img" aria-label="Rose filigree corner ornament"></div>

    <h1 class="insert__title">Directions</h1>
    <div class="insert__flourish" role="img" aria-label="Rose scroll flourish beneath the title"></div>

    <section class="directions directions--airport">
      <h2 class="directions__heading">FROM ..................AIRPORT - ......minutes/..........Km.</h2>
      <p class="directions__text">Lorem ipsum dolor sit amet, consectetur adipisicing elit, sed do eiusmod<br>tempor incididunt ut labore et dolore magna aliqua. Ut enim ad minim<br>veniam, quis nostrud exercitation ullamco laboris nisi ut aliquip ex ea<br>commodo consequa.Lorem ipsum dolor sit amet, consectetur adipisicing.</p>
    </section>

    <section class="directions directions--driving">
      <h2 class="directions__heading">DRIVING DIRECTIONS:</h2>
      <p class="directions__text">Lorem ipsum dolor sit amet, consectetur adipisicing elit, sed do eiusmod<br>tempor incididunt ut labore et dolore magna aliqua. Ut enim ad minim<br>veniam, quis nostrud exercitation ullamco laboris nisi ut aliquip ex ea<br>commodo consequa.Lorem ipsum dolor sit amet, consectetur adipisicing.</p>
    </section>
  </main>
</body>
</html>
```